Merge product image and small book on 1 photo

Hello

I have an order to place. It involves adding a small book to two measuring devices. Specifically, we need 1 picture each, on which the measuring device and the small book are shown together.

I have illustrated the various combinations in the "Yur job" file. It is your job to create the mockups professionally. You can find the contents of the mockups in the PDF. The page numbers of the pages you can use are noted in the "Your-Job" file.

There are 2 pictures showing the original book: It is A6 sized (15 cm high) and is not very thick (0.5 cm). The two measuring devices are larger. It simply has to look good so that we can present the pictures on the website.

You are welcome to use your own booklet compositions (with AI) or other techniques and do not necessarily have to use the templates. For example, where the book is illustrated with rotating pages - I can certainly use more templates there.

Many thanks in advance.

Best, Gerold

```html
<!DOCTYPE html>
<html lang="de">
<head>
<meta charset="utf-8">
<title>Ratgeber – Kinderzimmer mit Messgerät</title>
<link href="https://fonts.googleapis.com/css2?family=Roboto+Condensed:wght@400;700&display=swap" rel="stylesheet">
<style>
  :root {
    --red: #d63a30;
    --ink: #2b2b2b;
    --paper: #ffffff;
    --panel: #ececec;
    --bg: #e6e6e8;
    --photo-a: #d9c6b0;
    --photo-b: #f1ede8;
    --photo-c: #c9a783;
    --device-a: #fafafa;
    --device-b: #dcdcdc;
  }
  * { margin: 0; padding: 0; box-sizing: border-box; }
  html, body { width: 1200px; height: 1154px; overflow: hidden; }
  body {
    position: relative;
    background: var(--bg);
    font-family: "Roboto Condensed", Arial, sans-serif;
    color: var(--ink);
  }
  .spread {
    position: absolute; display: flex; width: 620px; height: 440px;
    box-shadow: 0 16px 34px rgba(0,0,0,.18);
  }
  .spread-top { left: 120px; top: 80px; }
  .spread-bottom { left: 440px; top: 570px; }
  .page { position: relative; width: 310px; height: 440px; background: var(--paper); overflow: hidden; }
  .page-curve { position: absolute; top: 0; left: 0; width: 310px; height: 80px; }
  .page-body { position: absolute; top: 84px; left: 30px; right: 22px; }
  .section-title { font-weight: 700; font-size: 12px; text-transform: uppercase; margin-bottom: 5px; }
  .tips { list-style: none; font-size: 10.5px; line-height: 1.32; }
  .tips li { position: relative; padding-left: 14px; }
  .tips li::before { content: "•"; position: absolute; left: 2px; }
  .callout { display: flex; align-items: center; gap: 8px; margin-top: 10px; font-size: 11px; }
  .callout svg { flex: none; }
  .distance-box {
    position: absolute; left: 0; right: 0; top: 322px; height: 118px;
    background: var(--panel); padding: 14px 22px 0 30px;
  }
  .distance-box p { font-size: 10px; line-height: 1.4; }
  .page-footer {
    position: absolute; bottom: 12px; display: flex; align-items: center; gap: 8px;
    font-weight: 700; font-size: 11px; text-transform: uppercase;
  }
  .page-footer .url { color: var(--red); text-transform: none; }
  .page-number { background: var(--red); color: #fff; padding: 2px 12px; font-size: 10.5px; }
  .page-left .page-footer { left: 0; }
  .page-right .page-footer { right: 0; }
  .page-right .page-footer .page-number { order: 2; }
  .photo {
    position: absolute; inset: 0;
    background: linear-gradient(160deg, var(--photo-a) 0%, var(--photo-b) 55%, var(--photo-c) 100%);
  }
  .device {
    position: absolute; left: 905px; top: 675px; width: 240px; height: 450px;
    border-radius: 26px;
    background: linear-gradient(150deg, var(--device-a) 0%, var(--device-b) 100%);
    box-shadow: 0 18px 36px rgba(0,0,0,.22);
  }
</style>
</head>
<body>
  <main class="spread spread-top">
    <section class="page page-left">
      <svg class="page-curve" viewBox="0 0 310 80" aria-hidden="true">
        <path d="M0 0 H310 C260 38 140 68 0 74 Z" fill="var(--red)"/>
      </svg>
      <div class="page-body">
        <h2 class="section-title">Kinderzimmer</h2>
        <ul class="tips">
          <li>Stellen Sie das Kinderbett 10 cm weg von der Wand.</li>
          <li>Ziehen Sie Kabel von Klemmlampen nicht unters oder um das Kinderbett.</li>
          <li>Babyphon: Der Abstand zum schlafenden Kind sollte mindestens zwei Meter betragen.</li>
          <li>Spielsachen und Geräte, die mit Batterien betrieben sind, erzeugen nur schwache Felder.</li>
          <li>Wenn Sie trotzdem einen Recorder mit Kabel haben: Stecker nach Gebrauch immer herausziehen.</li>
          <li>Das gilt auch für elektrisch betriebenes Spielzeug wie Rennbahn oder Eisenbahn. Platzieren Sie die Trafos möglichst weit weg vom Kinderbett.</li>
          <li>Verzichten Sie auf Halogenlampen (Transformator).</li>
          <li>Begrenzen Sie die TV- und Bildschirmzeit.</li>
        </ul>
        <p class="callout">
          <svg width="16" height="14" viewBox="0 0 26 22" aria-hidden="true">
            <path d="M2 2 L10 11 L2 20 M13 2 L21 11 L13 20" fill="none" stroke="var(--red)" stroke-width="4"/>
          </svg>
          Prävention ist wichtig – vor allem bei den Jüngsten
        </p>
      </div>
      <div class="distance-box">
        <h2 class="section-title">Abstand halten</h2>
        <p>Achten Sie darauf, dass im Zimmer Ihrer Kinder zu elektrischen Geräten mindestens ein Meter Abstand besteht. Dadurch verringern Sie die Belastung durch Elektrosmog erheblich.</p>
      </div>
      <footer class="page-footer">
        <span class="page-number">28</span>
        <span>Ratgeber <span class="url">www.feldrat.ch</span></span>
      </footer>
    </section>
    <section class="page page-right">
      <div class="photo" role="img" aria-label="Foto: Familie mit zwei Kindern schläft gemeinsam im Bett"></div>
      <svg class="page-curve" viewBox="0 0 310 80" aria-hidden="true">
        <path d="M0 0 H310 V44 C205 56 90 46 0 24 Z" fill="var(--red)"/>
      </svg>
      <footer class="page-footer">
        <span class="page-number">29</span>
        <span>Ratgeber <span class="url">www.feldrat.ch</span></span>
      </footer>
    </section>
  </main>

  <main class="spread spread-bottom">
    <section class="page page-left">
      <svg class="page-curve" viewBox="0 0 310 80" aria-hidden="true">
        <path d="M0 0 H310 C260 38 140 68 0 74 Z" fill="var(--red)"/>
      </svg>
      <div class="page-body">
        <h2 class="section-title">Kinderzimmer</h2>
        <ul class="tips">
          <li>Stellen Sie das Kinderbett 10 cm weg von der Wand.</li>
          <li>Ziehen Sie Kabel von Klemmlampen nicht unters oder um das Kinderbett.</li>
          <li>Babyphon: Der Abstand zum schlafenden Kind sollte mindestens zwei Meter betragen.</li>
          <li>Spielsachen und Geräte, die mit Batterien betrieben sind, erzeugen nur schwache Felder.</li>
          <li>Wenn Sie trotzdem einen Recorder mit Kabel haben: Stecker nach Gebrauch immer herausziehen.</li>
          <li>Das gilt auch für elektrisch betriebenes Spielzeug wie Rennbahn oder Eisenbahn. Platzieren Sie die Trafos möglichst weit weg vom Kinderbett.</li>
          <li>Verzichten Sie auf Halogenlampen (Transformator).</li>
          <li>Begrenzen Sie die TV- und Bildschirmzeit.</li>
        </ul>
        <p class="callout">
          <svg width="16" height="14" viewBox="0 0 26 22" aria-hidden="true">
            <path d="M2 2 L10 11 L2 20 M13 2 L21 11 L13 20" fill="none" stroke="var(--red)" stroke-width="4"/>
          </svg>
          Prävention ist wichtig – vor allem bei den Jüngsten
        </p>
      </div>
      <div class="distance-box">
        <h2 class="section-title">Abstand halten</h2>
        <p>Achten Sie darauf, dass im Zimmer Ihrer Kinder zu elektrischen Geräten mindestens ein Meter Abstand besteht. Dadurch verringern Sie die Belastung durch Elektrosmog erheblich.</p>
      </div>
      <footer class="page-footer">
        <span class="page-number">28</span>
        <span>Ratgeber <span class="url">www.feldrat.ch</span></span>
      </footer>
    </section>
    <section class="page page-right">
      <div class="photo" role="img" aria-label="Foto: Familie mit zwei Kindern schläft gemeinsam im Bett"></div>
      <svg class="page-curve" viewBox="0 0 310 80" aria-hidden="true">
        <path d="M0 0 H310 V44 C205 56 90 46 0 24 Z" fill="var(--red)"/>
      </svg>
      <footer class="page-footer">
        <span class="page-number">29</span>
        <span>Ratgeber <span class="url">www.feldrat.ch</span></span>
      </footer>
    </section>
  </main>

  <div class="device" role="img" aria-label="Produktfoto: weisses Handmessgerät für magnetische, elektrische und Hochfrequenz-Felder mit LED-Anzeigen"></div>
</body>
</html>
```